Learning Habits- Teaching and Learning Policy

Hi,

The philosophy behind this Teaching and Learning Policy is to equip young people (Age 16-18) for many challenges that lies ahead. The pace of technological advancement is so great that it is probable that many jobs our students will do in their lifetime do not yet even exist. We realise that we need to help develop our students into effective lifelong learners – meaning that they will:

-Need to be independent whilst also being able to work as a team.
-Need to apply many different strategies to help take on new concepts.
-Reflect on current practice, and improve.

I have attached the file which has the basic designs of the 4 different leaner habits and what they entail. Each habit is colour coordinated, so please keep the colours the same.

Collaboration- Blue (royal blue)
Persevering- Red
Planning- Orange
Reflection- Yellow

I would ideally like the poster to be transferable into a powerpoint too.

Thanking you all so much.

Lenka
Updates

Project Deadline Extended Reason: Hi,I am extending this deadline as I will be requesting some changes to the title / slogan.I need the four learning habits have a catchy name which will motivate students.Please send me some suggestions.Thanking you all.Lenka Added Monday, March 28, 2016

Target Market(s)

Teachers and students (age 16-18)

Industry/Entity Type

Education

Font styles to use
Other font styles liked:
• Something friendly to kids- where the a is printed like it is written. Similar to century gothic but more friendly.

Requirements
Must have
• Laid out similar to the the website attached. Interesting, motivational yet educational to students in how they can become lifelong learners.
Nice to have
• I should be able to transfer this to a powerpoint from a poster.
• It can be four posters or one depending on the design.
Should not have
• Each Habit must be colour-coordinated:
• Collaboration- Blue (royal blue)
• Persevering- Red
• Planning- Orange
• Reflection- Yellow
• Thank you,

```html
<!DOCTYPE html>
<html lang="en">
<head>
<meta charset="utf-8">
<title>Learning Habits – Teaching and Learning Posters</title>
<link rel="stylesheet" href="https://fonts.googleapis.com/css2?family=Ubuntu:wght@400;500;700&display=swap">
<style>
  :root {
    --page-bg: #ecebe9;
    --white: #ffffff;
    --ink-dark: #2e2e2e;

    --blue-start: #1592c4;
    --blue-end: #2b3ca8;
    --blue-badge: #2a3a9e;

    --yellow-start: #f3c318;
    --yellow-end: #e6e63c;
    --yellow-badge: #f1dc0f;

    --orange-start: #eb6a2c;
    --orange-end: #f1a21e;
    --orange-badge: #f0a020;

    --red-start: #c41f30;
    --red-end: #dc3b3a;
    --red-badge: #c21e34;
  }

  * { box-sizing: border-box; margin: 0; padding: 0; }

  html, body {
    width: 873px;
    height: 1200px;
    overflow: hidden;
    background: var(--page-bg);
    font-family: "Ubuntu", "Trebuchet MS", sans-serif;
  }

  .poster-set {
    width: 873px;
    height: 1200px;
    display: grid;
    grid-template-columns: 370px 370px;
    grid-template-rows: 520px 520px;
    column-gap: 45px;
    row-gap: 60px;
    padding: 50px 44px;
  }

  .habit-poster {
    position: relative;
    width: 370px;
    height: 520px;
    background: var(--white);
    box-shadow: 0 2px 8px rgba(0, 0, 0, 0.12);
    overflow: hidden;
  }

  .poster-shapes {
    position: absolute;
    inset: 0;
    width: 100%;
    height: 100%;
  }

  .habit-badge {
    position: absolute;
    left: 50%;
    top: 166px;
    width: 138px;
    height: 138px;
    margin: -69px 0 0 -69px;
    border-radius: 50%;
    display: flex;
    flex-direction: column;
    align-items: center;
    justify-content: center;
    gap: 7px;
    color: var(--white);
  }

  .habit-title {
    font-weight: 700;
    font-size: 18px;
    letter-spacing: -0.2px;
  }

  .habit-icon {
    width: 34px;
    height: 28px;
    border-radius: 3px;
  }

  .habit-skills {
    position: absolute;
    left: 0;
    right: 0;
    top: 300px;
    height: 124px;
    display: flex;
    flex-direction: column;
    align-items: center;
    justify-content: center;
    list-style: none;
    color: var(--white);
    font-size: 14px;
    font-weight: 500;
    line-height: 29px;
  }

  .collaboration .habit-badge { background: var(--blue-badge); }
  .collaboration .habit-icon { background: #6f7bc6; }

  .reflection .habit-badge { background: var(--yellow-badge); color: var(--ink-dark); }
  .reflection .habit-skills { color: var(--ink-dark); }
  .reflection .habit-icon { background: #b9a80f; }

  .planning .habit-badge { background: var(--orange-badge); }
  .planning .habit-icon { background: #f7c773; }

  .persevering .habit-badge { background: var(--red-badge); }
  .persevering .habit-icon { background: #de7c86; }
</style>
</head>
<body>
<main class="poster-set">

  <!-- Collaboration -->
  <section class="habit-poster collaboration">
    <svg class="poster-shapes" viewBox="0 0 245 345" preserveAspectRatio="none" aria-hidden="true">
      <defs>
        <linearGradient id="grad-blue" x1="0" x2="1" y1="0" y2="0">
          <stop offset="0" stop-color="var(--blue-start)"/>
          <stop offset="1" stop-color="var(--blue-end)"/>
        </linearGradient>
      </defs>
      <rect width="245" height="345" fill="url(#grad-blue)"/>
      <path d="M0,28 C70,2 150,34 245,14 L245,176 L190,200 L0,165 Z" fill="var(--white)"/>
      <path d="M0,307 L65,282 L245,300 L245,345 L0,345 Z" fill="var(--white)"/>
    </svg>
    <div class="habit-badge">
      <h2 class="habit-title">Collaboration</h2>
      <div class="habit-icon" role="img" aria-label="Pictogram of three people standing together"></div>
    </div>
    <ul class="habit-skills">
      <li>Empathy and Listening</li>
      <li>Interdependence</li>
      <li>Communication</li>
      <li>Questioning</li>
    </ul>
  </section>

  <!-- Reflection -->
  <section class="habit-poster reflection">
    <svg class="poster-shapes" viewBox="0 0 245 345" preserveAspectRatio="none" aria-hidden="true">
      <defs>
        <linearGradient id="grad-yellow" x1="0" x2="1" y1="0" y2="0">
          <stop offset="0" stop-color="var(--yellow-start)"/>
          <stop offset="1" stop-color="var(--yellow-end)"/>
        </linearGradient>
      </defs>
      <rect width="245" height="345" fill="url(#grad-yellow)"/>
      <path d="M0,28 C70,2 150,34 245,14 L245,176 L190,200 L0,165 Z" fill="var(--white)"/>
      <path d="M0,307 L65,282 L245,300 L245,345 L0,345 Z" fill="var(--white)"/>
    </svg>
    <div class="habit-badge">
      <h2 class="habit-title">Reflection</h2>
      <div class="habit-icon" role="img" aria-label="Pictogram of two speech bubbles"></div>
    </div>
    <ul class="habit-skills">
      <li>Monitoring</li>
      <li>Evaluating</li>
    </ul>
  </section>

  <!-- Planning -->
  <section class="habit-poster planning">
    <svg class="poster-shapes" viewBox="0 0 245 345" preserveAspectRatio="none" aria-hidden="true">
      <defs>
        <linearGradient id="grad-orange" x1="0" x2="1" y1="0" y2="0">
          <stop offset="0" stop-color="var(--orange-start)"/>
          <stop offset="1" stop-color="var(--orange-end)"/>
        </linearGradient>
      </defs>
      <rect width="245" height="345" fill="url(#grad-orange)"/>
      <path d="M0,28 C70,2 150,34 245,14 L245,176 L190,200 L0,165 Z" fill="var(--white)"/>
      <path d="M0,307 L65,282 L245,300 L245,345 L0,345 Z" fill="var(--white)"/>
    </svg>
    <div class="habit-badge">
      <h2 class="habit-title">Planning</h2>
      <div class="habit-icon" role="img" aria-label="Pictogram of a teacher pointing at a board"></div>
    </div>
    <ul class="habit-skills">
      <li>Distiling</li>
    </ul>
  </section>

  <!-- Persevering -->
  <section class="habit-poster persevering">
    <svg class="poster-shapes" viewBox="0 0 245 345" preserveAspectRatio="none" aria-hidden="true">
      <defs>
        <linearGradient id="grad-red" x1="0" x2="1" y1="0" y2="0">
          <stop offset="0" stop-color="var(--red-start)"/>
          <stop offset="1" stop-color="var(--red-end)"/>
        </linearGradient>
      </defs>
      <rect width="245" height="345" fill="url(#grad-red)"/>
      <path d="M0,28 C70,2 150,34 245,14 L245,176 L190,200 L0,165 Z" fill="var(--white)"/>
      <path d="M0,307 L65,282 L245,300 L245,345 L0,345 Z" fill="var(--white)"/>
    </svg>
    <div class="habit-badge">
      <h2 class="habit-title">Persevering</h2>
      <div class="habit-icon" role="img" aria-label="Pictogram of a person climbing a wall"></div>
    </div>
    <ul class="habit-skills">
      <li>Managing distractions</li>
      <li>Meta-Learning</li>
    </ul>
  </section>

</main>
</body>
</html>
```